Crypto Exchange Comparison Platform

Let’s design a page that lets users compare hundreds of cryptocurrency exchanges. It will help users compare more info than anywhere else so you can find the best crypto exchange for your needs. The goal is to transform complex data into a clean, visually engaging experience.

Key Features to Design:
- Interactive comparison table with ~ 30 columns
- Filters and dropdown menus for easier usability
- Summary boxes for quick-view statistics
- Visual charts and graphs for key metrics
- Web, mobile, and tablet responsive design

Design Goals:
- Clean, modern aesthetic that makes complex data easily digestible
- Interactive elements (eg. Bar and Spider charts) for user engagement
- "Screenshot-friendly" sections for social media and sharing
- Data visualization focus (charts, graphs, metrics)
- Extremely easy to use on mobile
- Designs that use the color green
- A brand that communicates research and trusted information

Deliverables:
- High-fidelity mockup for desktop, tablet, and mobile versions
- Interactive prototype (Figma preferred)
- Style guide (typography, colors, components)

Note: The goal is to create an intuitive, visually engaging tool that helps users compare cryptocurrency exchanges efficiently while maintaining a clean, professional appearance that works well for social media sharing and content creation.
Updates

Low design quality

Industry/Entity Type

FinTech, Crypto, Finance

Number of Pages Required

1 page

Other font styles liked:
• Inter or something good for a finance/data related website site

Colors
00AB8E
00BBA5
67D7C9
C6EFE9
E9F9F6

Requirements
Must have
• Please refer to the sketch I uploaded

```html
<!DOCTYPE html>
<html lang="en">
<head>
<meta charset="utf-8">
<title>Crypto exchange — Compare Crypto Exchanges</title>
<link rel="stylesheet" href="https://fonts.googleapis.com/css2?family=Poppins:wght@400;500;600;700&display=swap">
<style>
:root{
  --navy:#070c3f;
  --navy-deep:#03062a;
  --blue:#1c3cff;
  --blue-bright:#2e5bff;
  --sky:#3f93ff;
  --cyan:#4ee6f0;
  --teal:#2bb3a8;
  --green:#00bba5;
  --green-soft:#e9f9f6;
  --red:#ff2d55;
  --ink:#0b0f2e;
  --muted:#6b7090;
  --row:#f3f5fc;
  --line:#e6e9f4;
  --white:#ffffff;
}
*{box-sizing:border-box;margin:0;padding:0}
html,body{width:1200px;height:4092px;overflow:hidden}
body{font-family:"Poppins",Arial,sans-serif;color:var(--ink);background:var(--white);position:relative}
.abs{position:absolute}
.page-bg{position:absolute;left:0;top:0;width:1200px;height:760px;
  background:
    radial-gradient(ellipse 700px 420px at 1000px 260px,rgba(46,91,255,.95),rgba(46,91,255,0) 70%),
    linear-gradient(180deg,var(--navy) 0px,#13237f 220px,#4a63ef 380px,#c8d1ff 560px,#ffffff 760px);}
.brand{left:86px;top:26px;font-size:24px;font-weight:700;color:var(--white)}
.nav{left:580px;top:31px;font-size:14px;color:var(--white)}
.nav a{color:inherit;text-decoration:none;position:absolute;white-space:nowrap}
.hero-title{left:86px;top:212px;font-size:54px;font-weight:700;line-height:57px;color:var(--white)}
.hero-sub{left:86px;top:336px;font-size:14px;line-height:20px;color:var(--white);width:460px}
.hero-meta{left:86px;top:382px;font-size:14px;color:var(--white);display:flex;gap:20px}
.hero-meta b{font-weight:600}
.btn{display:flex;align-items:center;justify-content:center;border-radius:30px;background:var(--blue);color:var(--white);font-weight:500;font-size:14px}
.hero-btn{left:86px;top:423px;width:159px;height:44px;box-shadow:0 6px 18px rgba(28,60,255,.35)}
.hero-art{left:636px;top:175px;width:508px;height:397px;border-radius:24px;
  background:radial-gradient(circle at 55% 45%,rgba(160,180,255,.75),rgba(70,100,255,.35) 55%,rgba(70,100,255,0) 75%)}
.section-title{font-size:44px;color:var(--ink);text-align:center;width:1200px;left:0}
.section-title b{font-weight:700}
.section-title span{font-weight:400}
.pick{width:187px;height:178px;top:680px;background:rgba(255,255,255,.78);border-radius:14px;padding:0 29px}
.pick .ico{position:absolute;left:29px;top:26px;width:34px;height:34px;border-radius:50%;background:var(--white);box-shadow:0 2px 8px rgba(20,30,90,.12);display:flex;align-items:center;justify-content:center}
.pick .ico i{width:16px;height:16px;border-radius:50%;background:var(--ink);display:block}
.pick .name{position:absolute;left:29px;top:70px;font-size:15px;font-weight:600}
.pick .price{position:absolute;left:29px;top:92px;font-size:13px;color:var(--muted)}
.pick .chg{position:absolute;left:29px;top:132px;font-size:20px;display:flex;align-items:center;gap:8px}
.tri-up{width:0;height:0;border-left:10px solid transparent;border-right:10px solid transparent;border-bottom:16px solid var(--green)}
.tri-down{width:0;height:0;border-left:10px solid transparent;border-right:10px solid transparent;border-top:16px solid var(--red)}
.tab{top:928px;height:45px;display:flex;align-items:center;font-size:14px;font-weight:500}
.tab.active{background:var(--ink);color:var(--white);border-radius:24px;justify-content:center;width:109px;left:87px}
.compare-btn{left:1001px;top:928px;width:108px;height:45px}
.fee-table{left:90px;top:996px;width:1019px;border-collapse:collapse;font-size:10.5px;box-shadow:0 6px 24px rgba(20,30,90,.05)}
.fee-table th{height:53px;font-weight:500;font-size:9px;text-align:left;color:var(--ink)}
.fee-table td{height:57.7px;font-weight:500}
.fee-table tbody tr:nth-child(even){background:var(--row)}
.fee-table .red{color:var(--red);font-weight:400}
.fee-table .grn{color:var(--green);font-weight:400}
.fee-table .coin{display:inline-flex;align-items:center;gap:6px;font-weight:600;font-size:10px}
.fee-table .coin i{width:15px;height:15px;border-radius:50%;display:inline-block}
.fee-table .coin small{font-weight:400;color:var(--muted);font-size:9.5px}
.fee-table .bonus{line-height:12px;font-size:10px}
.star{display:inline-block;width:13px;height:13px;vertical-align:middle;margin-right:12px}
.pager{top:1488px;height:28px;font-size:11px;display:flex;align-items:center}
.pg-prev{left:445px;width:75px;border-radius:16px;background:#f1f2f7;justify-content:center;color:var(--muted)}
.pg-num{position:absolute;top:1496px;font-size:11px}
.pg-cur{left:558px;top:1487px;width:30px;height:30px;border-radius:50%;background:var(--blue);color:var(--white);display:flex;align-items:center;justify-content:center;font-size:11px}
.pg-next{left:680px;width:76px;border-radius:16px;background:var(--blue);color:var(--white);justify-content:center;font-weight:500}
.chart-card{top:1597px;width:382px;height:345px;background:var(--white);border-radius:14px;box-shadow:0 8px 30px rgba(20,30,90,.08)}
.chart-card h3{position:absolute;left:35px;top:28px;font-size:27px;font-weight:600}
.chart-card h3 span{font-weight:400}
.chart-card svg{position:absolute;left:0;top:0}
.stats{left:89px;top:2000px;width:1020px;height:480px}
.stat{position:absolute;text-align:center;color:var(--white);width:240px}
.stat .lbl{font-size:15px;font-weight:500}
.stat .num{font-size:48px;font-weight:700;line-height:60px;margin-top:6px}
.cmp-title{left:159px;top:2530px;font-size:45px;font-weight:700}
.dd{top:2558px;font-size:14px;font-weight:500;display:flex;align-items:center;gap:8px}
.radar{left:136px;top:2630px}
.score-card{left:152px;top:2937px;width:414px;height:270px;background:var(--row);border-radius:14px}
.score-card table{position:absolute;left:12px;top:20px;width:390px;border-collapse:collapse;font-size:11px}
.score-card th{font-weight:500;height:22px;text-align:left}
.score-card td{height:38px}
.score-card tbody tr:nth-child(even) td{background:var(--white)}
.acc{left:601px;width:468px;border:1px solid var(--line);border-radius:6px;background:var(--white)}
.acc h4{position:absolute;left:26px;font-size:18px;font-weight:600}
.acc .sign{position:absolute;right:26px;font-size:22px;font-weight:400}
.feat-row{position:absolute;left:14px;width:436px;height:32px;font-size:10.5px;display:flex;align-items:center;border-radius:4px}
.feat-row .k{position:absolute;left:14px}
.feat-row .a{position:absolute;left:258px;display:flex;align-items:center;gap:8px}
.feat-row .b{position:absolute;left:370px;display:flex;align-items:center;gap:8px}
.up-s{width:0;height:0;border-left:4px solid transparent;border-right:4px solid transparent;border-bottom:5px solid var(--green)}
.dn-s{width:0;height:0;border-left:4px solid transparent;border-right:4px solid transparent;border-top:5px solid var(--red)}
.full-btn{left:601px;top:3154px;width:170px;height:53px;font-size:14px}
.faq-item{left:315px;width:572px;height:48px;border-radius:4px;background:var(--row);display:flex;align-items:center;padding:0 27px;font-size:15px;font-weight:500;justify-content:space-between}
.faq-item.open{background:var(--blue);color:var(--white)}
.faq-item em{font-style:normal;font-size:20px;font-weight:400}
.footer{left:0;top:3655px;width:1200px;height:437px;
  background:linear-gradient(180deg,#2449f2 0px,#1a2fb8 90px,#0b1466 200px,var(--navy-deep) 437px)}
.nl-title{left:96px;top:3770px;font-size:24px;font-weight:700;line-height:28px;color:var(--white);width:460px}
.nl-sub{left:96px;top:3830px;font-size:14px;line-height:19px;color:var(--white);width:430px}
.nl-form{left:569px;top:3777px;width:548px;height:59px;border-radius:8px;overflow:hidden;display:flex}
.nl-form .field{flex:0 0 404px;background:rgba(255,255,255,.14);color:rgba(255,255,255,.7);font-size:14px;display:flex;align-items:center;padding-left:26px}
.nl-form .send{flex:1;background:var(--blue);color:var(--white);font-size:14px;font-weight:500;display:flex;align-items:center;justify-content:center}
.copy{left:90px;top:3932px;font-size:13px;color:#3b5cff}
.legal{left:90px;top:3958px;width:1010px;font-size:10.5px;line-height:16px;color:var(--white)}
</style>
</head>
<body>

<div class="page-bg"></div>

<div class="abs brand">Crypto exchange</div>
<nav class="abs nav" style="width:600px;height:20px">
  <a style="left:0">Cryptocurrencies</a>
  <a style="left:151px">PoolScope</a>
  <a style="left:246px">Exchanges</a>
  <a style="left:354px">Community</a>
  <a style="left:472px">Products</a>
</nav>

<h1 class="abs hero-title">Compare Crypto<br>Exchanges</h1>
<p class="abs hero-sub">Find the best cryptocurrency exchange with the most detailed and up-to-date comparison tool.</p>
<div class="abs hero-meta"><span>Platform Tracked : <b>125</b></span><span>Updated: <b>16,2025</b></span><span>How We Test &nbsp;›</span></div>
<div class="abs btn hero-btn">Start Trading</div>
<div class="abs hero-art" role="img" aria-label="Isometric illustration of a glowing blue processor chip carrying a large coin, surrounded by smaller chips with coins"></div>

<h2 class="abs section-title" style="top:600px"><b>Top</b> <span>Picks</span></h2>

<div class="abs pick" style="left:211px"><div class="ico"><i></i></div><div class="name">Nordcoin</div><div class="price">96,261.00 DWL</div><div class="chg"><span class="tri-up"></span>0.53 %</div></div>
<div class="abs pick" style="left:408px"><div class="ico"><i></i></div><div class="name">Lumera</div><div class="price">2,727.47 DWL</div><div class="chg"><span class="tri-up"></span>1.61 %</div></div>
<div class="abs pick" style="left:605px"><div class="ico"><i></i></div><div class="name">Solvane</div><div class="price">169.55 DWL</div><div class="chg"><span class="tri-up"></span>0.39 %</div></div>
<div class="abs pick" style="left:801px"><div class="ico"><i></i></div><div class="name">Verdex</div><div class="price">2.5573 DWL</div><div class="chg"><span class="tri-down"></span>-1.20 %</div></div>

<div class="abs tab active">Fees</div>
<div class="abs tab" style="left:215px">Features</div>
<div class="abs tab" style="left:313px">Security</div>
<div class="abs btn compare-btn">Compare</div>

<table class="abs fee-table">
  <colgroup>
    <col style="width:105px"><col style="width:167px"><col style="width:86px"><col style="width:84px"><col style="width:123px"><col style="width:119px"><col style="width:133px"><col style="width:124px"><col style="width:78px">
  </colgroup>
  <thead>
    <tr><th></th><th></th><th>Maker Fee</th><th>Taker Fee</th><th>Futures Maker Fee</th><th>Futures Taker Fee</th><th>Trading Fee Discounts</th><th>Discount or Bonus</th><th>Visit</th></tr>
  </thead>
  <tbody>
    <tr><td style="padding-left:22px"><svg class="star" viewBox="0 0 24 24"><path d="M12 2.5l2.9 6.1 6.6.8-4.9 4.6 1.3 6.6L12 17.3l-5.9 3.3 1.3-6.6L2.5 9.4l6.6-.8z" fill="none" stroke="#0b0f2e" stroke-width="1.8"/></svg>01</td><td><span class="coin"><i style="background:#f7931a"></i>Nordcoin <small>NRC</small></span></td><td class="red">(eg. 0.10%)</td><td class="grn">(eg. 0.20%)</td><td>Fee</td><td>Fee</td><td>(yes/no)</td><td class="bonus">(eg. 10% Off, or<br>$1,000 Bonus)</td><td>www.com</td></tr>
    <tr><td style="padding-left:22px"><svg class="star" viewBox="0 0 24 24"><path d="M12 2.5l2.9 6.1 6.6.8-4.9 4.6 1.3 6.6L12 17.3l-5.9 3.3 1.3-6.6L2.5 9.4l6.6-.8z" fill="none" stroke="#0b0f2e" stroke-width="1.8"/></svg>02</td><td><span class="coin"><i style="background:#3a3a4a"></i>Lumera <small>LMR</small></span></td><td>(eg. 0.10%)</td><td class="grn">(eg. 0.20%)</td><td>Fee</td><td>Fee</td><td>(yes/no)</td><td class="bonus">(eg. 10% Off, or<br>$1,000 Bonus)</td><td>www.com</td></tr>
    <tr><td style="padding-left:22px"><svg class="star" viewBox="0 0 24 24"><path d="M12 2.5l2.9 6.1 6.6.8-4.9 4.6 1.3 6.6L12 17.3l-5.9 3.3 1.3-6.6L2.5 9.4l6.6-.8z" fill="none" stroke="#0b0f2e" stroke-width="1.8"/></svg>03</td><td><span class="coin"><i style="background:#23292f"></i>Verdex <small style="color:#1c3cff">VDX</small></span></td><td class="red">(eg. 0.10%)</td><td class="red">(eg. 0.20%)</td><td>Fee</td><td>Fee</td><td>(yes/no)</td><td class="bonus">(eg. 10% Off, or<br>$1,000 Bonus)</td><td>www.com</td></tr>
    <tr><td style="padding-left:22px"><svg class="star" viewBox="0 0 24 24"><path d="M12 2.5l2.9 6.1 6.6.8-4.9 4.6 1.3 6.6L12 17.3l-5.9 3.3 1.3-6.6L2.5 9.4l6.6-.8z" fill="none" stroke="#0b0f2e" stroke-width="1.8"/></svg>04</td><td><span class="coin"><i style="background:#26a17b"></i>Steadyline <small>STL</small></span></td><td>(eg. 0.10%)</td><td class="grn">(eg. 0.20%)</td><td>Fee</td><td>Fee</td><td>(yes/no)</td><td class="bonus">(eg. 10% Off, or<br>$1,000 Bonus)</td><td>www.com</td></tr>
    <tr><td style="padding-left:22px"><svg class="star" viewBox="0 0 24 24"><path d="M12 2.5l2.9 6.1 6.6.8-4.9 4.6 1.3 6.6L12 17.3l-5.9 3.3 1.3-6.6L2.5 9.4l6.6-.8z" fill="none" stroke="#0b0f2e" stroke-width="1.8"/></svg>05</td><td><span class="coin"><i style="background:#f3ba2f"></i>Bexa <small>BXA</small></span></td><td>(eg. 0.10%)</td><td class="grn">(eg. 0.20%)</td><td>Fee</td><td>Fee</td><td>(yes/no)</td><td class="bonus">(eg. 10% Off, or<br>$1,000 Bonus)</td><td>www.com</td></tr>
    <tr><td style="padding-left:22px"><svg class="star" viewBox="0 0 24 24"><path d="M12 2.5l2.9 6.1 6.6.8-4.9 4.6 1.3 6.6L12 17.3l-5.9 3.3 1.3-6.6L2.5 9.4l6.6-.8z" fill="none" stroke="#0b0f2e" stroke-width="1.8"/></svg>06</td><td><span class="coin"><i style="background:#0b0f2e"></i>Solvane <small>SVN</small></span></td><td>(eg. 0.10%)</td><td>(eg. 0.20%)</td><td>Fee</td><td>Fee</td><td>(yes/no)</td><td class="bonus">(eg. 10% Off, or<br>$1,000 Bonus)</td><td>www.com</td></tr>
    <tr><td style="padding-left:22px"><svg class="star" viewBox="0 0 24 24"><path d="M12 2.5l2.9 6.1 6.6.8-4.9 4.6 1.3 6.6L12 17.3l-5.9 3.3 1.3-6.6L2.5 9.4l6.6-.8z" fill="none" stroke="#0b0f2e" stroke-width="1.8"/></svg>07</td><td><span class="coin"><i style="background:#2775ca"></i>Dollarwell <small>DWL</small></span></td><td>(eg. 0.10%)</td><td>(eg. 0.20%)</td><td>Fee</td><td>Fee</td><td>(yes/no)</td><td class="bonus">(eg. 10% Off, or<br>$1,000 Bonus)</td><td>www.com</td></tr>
  </tbody>
</table>

<div class="abs pager pg-prev">‹ &nbsp;Prev</div>
<span class="pg-num" style="left:539px">1</span>
<div class="abs pg-cur">2</div>
<span class="pg-num" style="left:598px">3</span>
<span class="pg-num" style="left:618px">...</span>
<span class="pg-num" style="left:638px">82</span>
<div class="abs pager pg-next">Next &nbsp;›</div>

<div class="abs chart-card" style="left:211px">
  <h3>Maker <span>Fees</span> <span style="font-size:16px">⌄</span></h3>
  <svg width="382" height="345" viewBox="0 0 382 345">
    <g stroke="#e3e6ef" stroke-width="1">
      <line x1="62" y1="297" x2="345" y2="297"/><line x1="62" y1="281" x2="345" y2="281"/><line x1="62" y1="265" x2="345" y2="265"/><line x1="62" y1="249" x2="345" y2="249"/><line x1="62" y1="233" x2="345" y2="233"/><line x1="62" y1="217" x2="345" y2="217"/><line x1="62" y1="201" x2="345" y2="201"/><line x1="62" y1="185" x2="345" y2="185"/><line x1="62" y1="169" x2="345" y2="169"/><line x1="62" y1="153" x2="345" y2="153"/><line x1="62" y1="137" x2="345" y2="137"/>
    </g>
    <g font-size="7" fill="#9aa0b6" text-anchor="end" font-family="Poppins,Arial,sans-serif">
      <text x="52" y="300">0%</text><text x="52" y="284">10%</text><text x="52" y="268">20%</text><text x="52" y="252">30%</text><text x="52" y="236">40%</text><text x="52" y="220">50%</text><text x="52" y="204">60%</text><text x="52" y="188">70%</text><text x="52" y="172">80%</text><text x="52" y="156">90%</text><text x="52" y="140">100%</text>
    </g>
    <g>
      <rect x="77" y="145" width="10" height="152" fill="#2946e8"/><rect x="88" y="137" width="10" height="160" fill="#4ee6f0"/><rect x="99" y="201" width="10" height="96" fill="#2bb3a8"/><rect x="110" y="265" width="10" height="32" fill="#b3b6bf"/>
      <rect x="141" y="201" width="10" height="96" fill="#2946e8"/><rect x="152" y="185" width="10" height="112" fill="#4ee6f0"/><rect x="163" y="173" width="10" height="124" fill="#2bb3a8"/><rect x="174" y="201" width="10" height="96" fill="#b3b6bf"/>
      <rect x="204" y="185" width="10" height="112" fill="#2946e8"/><rect x="215" y="153" width="10" height="144" fill="#4ee6f0"/><rect x="226" y="166" width="10" height="131" fill="#2bb3a8"/><rect x="237" y="201" width="10" height="96" fill="#b3b6bf"/>
      <rect x="268" y="137" width="10" height="160" fill="#2946e8"/><rect x="279" y="169" width="10" height="128" fill="#4ee6f0"/><rect x="290" y="185" width="10" height="112" fill="#2bb3a8"/><rect x="301" y="249" width="10" height="48" fill="#b3b6bf"/>
    </g>
    <g stroke="#999" stroke-width="1.5" fill="#999">
      <line x1="62" y1="300" x2="62" y2="98"/><path d="M58 102 L62 92 L66 102z"/>
      <line x1="60" y1="297" x2="350" y2="297"/><path d="M346 293 L356 297 L346 301z"/>
    </g>
  </svg>
</div>

<div class="abs chart-card" style="left:602px">
  <h3>Trading <span>Volume</span> <span style="font-size:16px">⌄</span></h3>
  <svg width="382" height="345" viewBox="0 0 382 345">
    <g font-size="10" fill="#9aa0b6" text-anchor="end" font-family="Poppins,Arial,sans-serif">
      <text x="44" y="141">70</text><text x="44" y="171">60</text><text x="44" y="202">50</text><text x="44" y="233">40</text><text x="44" y="263">30</text>
    </g>
    <g font-size="9" fill="#9aa0b6" font-family="Poppins,Arial,sans-serif">
      <text transform="translate(90,320) rotate(-55)">2011</text><text transform="translate(121,320) rotate(-55)">2012</text><text transform="translate(152,320) rotate(-55)">2013</text><text transform="translate(183,320) rotate(-55)">2014</text><text transform="translate(214,320) rotate(-55)">2015</text><text transform="translate(245,320) rotate(-55)">2016</text><text transform="translate(276,320) rotate(-55)">2017</text><text transform="translate(307,320) rotate(-55)">2018</text>
    </g>
    <g stroke="#999" stroke-width="1.5" fill="#999">
      <line x1="53" y1="295" x2="53" y2="98"/><path d="M49 102 L53 92 L57 102z"/>
      <line x1="51" y1="291" x2="345" y2="291"/><path d="M341 287 L351 291 L341 295z"/>
    </g>
    <g fill="none" stroke-width="3" stroke-linejoin="round">
      <polyline stroke="#1f3df0" points="53,168 86,137 117,168 148,137 179,137 210,199 241,137 272,214 304,199"/>
      <polyline stroke="#2bb3a8" points="53,245 86,199 117,260 148,199 179,229 210,137 241,199 272,168"/>
      <polyline stroke="#4ee6f0" points="53,276 86,229 117,214 148,214 179,199 210,229 241,168 272,168 304,137"/>
    </g>
    <g stroke="#fff" stroke-width="2">
      <g fill="#1f3df0"><circle cx="86" cy="137" r="5"/><circle cx="117" cy="168" r="5"/><circle cx="148" cy="137" r="5"/><circle cx="210" cy="199" r="5"/><circle cx="272" cy="214" r="5"/><circle cx="304" cy="199" r="5"/></g>
      <g fill="#2bb3a8"><circle cx="86" cy="199" r="5"/><circle cx="117" cy="260" r="5"/><circle cx="148" cy="199" r="5"/><circle cx="179" cy="229" r="5"/><circle cx="210" cy="137" r="5"/><circle cx="241" cy="199" r="5"/><circle cx="304" cy="168" r="5"/></g>
      <g fill="#4ee6f0"><circle cx="117" cy="214" r="5"/><circle cx="148" cy="214" r="5"/><circle cx="179" cy="199" r="5"/><circle cx="241" cy="168" r="5"/><circle cx="304" cy="137" r="5"/></g>
    </g>
  </svg>
</div>

<svg class="abs stats" width="1020" height="480" viewBox="0 0 1020 480" aria-hidden="true">
  <defs>
    <linearGradient id="bandGrad" x1="0" y1="0" x2="1" y2="1">
      <stop offset="0" stop-color="#050a45"/><stop offset=".55" stop-color="#0a1a9e"/><stop offset=".75" stop-color="#1634e6"/><stop offset="1" stop-color="#040830"/>
    </linearGradient>
    <linearGradient id="discGrad" x1="0" y1="0" x2="0" y2="1">
      <stop offset="0" stop-color="#3d95ff"/><stop offset=".3" stop-color="#1a46ff"/><stop offset="1" stop-color="#0f2cf0"/>
    </linearGradient>
    <clipPath id="discClip"><circle cx="510" cy="239" r="227"/></clipPath>
  </defs>
  <rect x="0" y="66" width="1020" height="341" rx="64" fill="url(#bandGrad)"/>
  <circle cx="510" cy="239" r="227" fill="url(#discGrad)"/>
  <polygon clip-path="url(#discClip)" points="660,66 1020,66 1020,480 320,480" fill="#0a1ed0" opacity=".85"/>
</svg>
<div class="stat" style="left:134px;top:2193px"><div class="lbl">Exchanges Tracked</div><div class="num">125</div></div>
<div class="stat" style="left:369px;top:2193px"><div class="lbl">Average Trading Fee</div><div class="num">0.15%</div></div>
<div class="stat" style="left:597px;top:2193px"><div class="lbl">Total Users</div><div class="num">892M</div></div>
<div class="stat" style="left:824px;top:2193px"><div class="lbl">Web Vistors (30D)</div><div class="num">12.2B</div></div>

<h2 class="abs cmp-title">Compare</h2>
<div class="abs dd" style="left:862px">Coinhaven <span style="font-size:12px">⌄</span></div>
<div class="abs dd" style="left:972px">Ledgerport <span style="font-size:12px;margin-left:14px">⌄</span></div>

<svg class="abs radar" width="460" height="300" viewBox="0 0 460 300" aria-label="Spider chart comparing two exchanges">
  <g font-size="13" fill="#0b0f2e" font-family="Poppins,Arial,sans-serif" font-weight="500">
    <text x="192" y="23">Fees</text><text x="18" y="114">Security</text><text x="345" y="114">Features</text><text x="14" y="236">Deposits</text><text x="346" y="236">Withdrawals</text>
  </g>
  <g fill="none" stroke="#5a8fc8" stroke-width="1">
    <polygon points="210,40 320,103.5 320,230.5 210,294 100,230.5 100,103.5"/>
    <polygon points="210,61 302,114 302,220 210,273 118,220 118,114"/>
    <polygon points="210,82 283,124 283,210 210,252 137,210 137,124"/>
    <polygon points="210,104 265,135.5 265,198.5 210,230 155,198.5 155,135.5"/>
    <polygon points="210,125 247,146 247,188 210,209 173,188 173,146"/>
    <polygon points="210,146 228,157 228,177 210,188 192,177 192,157"/>
    <line x1="210" y1="40" x2="210" y2="294"/><line x1="100" y1="103.5" x2="320" y2="230.5"/><line x1="320" y1="103.5" x2="100" y2="230.5"/>
  </g>
  <polygon points="210,52 305,112 313,226 210,280 108,224 112,118" fill="none" stroke="#f5d300" stroke-width="1.3"/>
  <polygon points="210,46 300,115 318,229 210,270 103,213 104,106" fill="none" stroke="#ff4b6b" stroke-width="1.3"/>
</svg>

<div class="abs score-card">
  <table>
    <thead><tr><th style="width:140px"></th><th style="width:120px">Coinhaven</th><th>Ledgerport</th></tr></thead>
    <tbody>
      <tr><td style="padding-left:31px">Fees</td><td>9/10</td><td>4/10</td></tr>
      <tr><td style="padding-left:31px">Security</td><td>9/10</td><td>4/10</td></tr>
      <tr><td style="padding-left:31px">Features</td><td>9/10</td><td>4/10</td></tr>
      <tr><td style="padding-left:31px">Deposits</td><td>9/10</td><td>4/10</td></tr>
      <tr><td style="padding-left:31px">Withdrawals</td><td>9/10</td><td>4/10</td></tr>
    </tbody>
  </table>
</div>

<div class="abs acc" style="top:2609px;height:251px">
  <h4 style="top:17px">Features</h4><span class="sign" style="top:12px">–</span>
  <div style="position:absolute;left:0;top:66px;width:468px;height:170px">
    <div class="feat-row" style="top:0;background:var(--row)"><span class="k"># of Coins</span><span class="a"><i class="up-s"></i>123%</span><span class="b"><i class="dn-s"></i>100%</span></div>
    <div class="feat-row" style="top:35px;background:var(--green-soft)"><span class="k"># of Futures</span><span class="a"><i class="up-s"></i>04%</span><span class="b"><i class="dn-s"></i>02%</span></div>
    <div class="feat-row" style="top:70px;background:var(--white)"><span class="k">Trading Bots</span><span class="a"><i class="up-s"></i>12345</span><span class="b"><i class="dn-s"></i>-</span></div>
    <div class="feat-row" style="top:105px;background:var(--row)"><span class="k">Copy Trading</span><span class="a"><i class="up-s"></i>123456</span><span class="b"><i class="dn-s"></i>-</span></div>
    <div class="feat-row" style="top:140px;background:var(--white)"><span class="k">24/7 Support</span><span class="a"><i class="up-s"></i>12345</span><span class="b"><i class="dn-s"></i>1245</span></div>
  </div>
</div>
<div class="abs acc" style="top:2879px;height:61px"><h4 style="top:17px">Security</h4><span class="sign" style="top:13px">+</span></div>
<div class="abs acc" style="top:2944px;height:61px"><h4 style="top:17px">Fees</h4><span class="sign" style="top:13px">+</span></div>
<div class="abs acc" style="top:3010px;height:61px"><h4 style="top:17px">Deposits</h4><span class="sign" style="top:13px">+</span></div>
<div class="abs acc" style="top:3075px;height:60px"><h4 style="top:17px">Withdrawals</h4><span class="sign" style="top:13px">+</span></div>
<div class="abs btn full-btn">Full Comparison</div>

<h2 class="abs section-title" style="top:3266px;font-weight:700">FAQ</h2>
<div class="abs faq-item" style="top:3343px">How is this data tracked?<em>+</em></div>
<div class="abs faq-item" style="top:3400px">How often is this page updated?<em>+</em></div>
<div class="abs faq-item open" style="top:3458px">What Are Crypto Exchanges?<em>+</em></div>
<div class="abs faq-item" style="top:3515px">How To Choose a Crypto Exchange?<em>+</em></div>

<footer class="abs footer"></footer>
<h3 class="abs nl-title">Interested to stay up-to-date with cryptocurrencies?</h3>
<p class="abs nl-sub">Get the latest crypto news, updates, and reports by subscribing to our free newsletter.</p>
<div class="abs nl-form"><div class="field">Enter your email address</div><div class="send">Subscribe</div></div>
<p class="abs copy">© 2025 crypto exchange . All Rights Reserved.</p>
<p class="abs legal">crypto exchange: All content provided herein our website, hyperlinked sites, associated applications, forums, blogs, social media accounts and other platforms ("Site") is for your general information only, procured from third party sources. We make no warranties of any kind in relation to our content, including but not limited to accuracy and updatedness. No part of the content that we provide constitutes financial advice, legal advice or any other form of advice meant for your specific reliance for any purpose. Any use or reliance on our content is solely at your own risk and discretion. You should conduct your own research, review, analyse and verify our content before relying on them. Trading is a highly risky activity that can lead to major losses, please therefore consult your financial advisor before making any decision. No content on our Site is meant to be a solicitation or offer.</p>

</body>
</html>
```